Nutrient Guild of Meridia Website Creation

Nutrient Guild of Meridia seeks a membership website that is visually dynamic, suitable for all who seek knowledge and inspiration about maximizing their health and wellbeing. see nutrientguildofmeridia.com

Target Market(s)

Scientists, Media, Medical Professionals, Nutritionists, Public

Industry/Entity Type

Nutrition

Number of Pages Required

5+ page

Font styles to use
Sans Serif

Colors
0355a3
ec1f27

Requirements
Must have
• Large Pictures, full screen
• Areas for video, blog, articles
• Membership sign in/ Public Access
• Easy to Edit/Add Content
• Merchant Ready
• please check out http://greenleafcircle.org This is what I want it to resemble.
Nice to have
• Red White and Blue but not static, old fashioned, but upbeat.
• Movement - subtle
Should not have
• Should not look Governmental-ish
• Flat look
• Small page
• should not look like the basic site at www.nutrientguildofmeridia.com

```html
<!DOCTYPE html>
<html lang="en">
<head>
<meta charset="utf-8">
<title>Nutrient Guild of Meridia</title>
<link href="https://fonts.googleapis.com/css2?family=Open+Sans:wght@400;600;700&display=swap" rel="stylesheet">
<style>
:root{
  --blue:#0355a3;
  --blue-dark:#0a3b78;
  --navy:#0b2f63;
  --red:#ec1f27;
  --ink:#333;
  --muted:#666;
  --light:#f2f4f7;
  --white:#fff;
}
*{box-sizing:border-box;margin:0;padding:0}
html,body{width:684px;height:1200px;overflow:hidden}
body{font-family:'Open Sans',Arial,sans-serif;color:var(--ink);background:var(--white);font-size:7px;line-height:1.45}
.wrap{padding:0 40px}
.btn{display:inline-block;color:var(--white);font-size:7px;font-weight:600;padding:4px 11px;border-radius:1px}
.btn-blue{background:var(--blue)}
.btn-red{background:var(--red)}

/* header */
.site-header{height:50px;display:flex;align-items:center;justify-content:space-between;padding:0 32px}
.brand{display:flex;align-items:center;gap:8px}
.brand-mark{width:36px;height:36px;border-radius:50%;background:var(--blue)}
.brand-name{font-size:10px;font-weight:700;color:var(--blue)}
.header-tools{display:flex;flex-direction:column;align-items:flex-end;gap:4px}
.login{background:var(--red);color:var(--white);font-size:7px;font-weight:600;padding:3px 14px}
.search{display:flex;align-items:center;border:1px solid #ccc;width:90px;height:11px;justify-content:flex-end;padding-right:2px}

/* hero */
.hero{height:206px;position:relative;background:linear-gradient(100deg,#f7f3ee 0%,#e9ddd0 35%,#cfd9c2 55%,#e7c9b4 75%,#d9b59c 100%);display:flex;align-items:center;justify-content:center}
.hero-title{font-size:20px;font-weight:400;color:var(--white);text-shadow:0 1px 3px rgba(0,0,0,.35);margin-right:80px}

/* nav */
.main-nav{height:26px;background:var(--blue);display:flex;padding-left:60px}
.main-nav a{color:var(--white);font-size:7px;font-weight:600;padding:0 11px;display:flex;align-items:center;border-right:1px solid rgba(255,255,255,.25)}
.main-nav a.active{background:var(--red)}

/* founding */
.founding{height:148px;text-align:center;padding-top:14px}
.section-title{font-size:15px;font-weight:600;color:var(--blue)}
.founding .sub{font-size:8px;font-weight:600;color:var(--ink);margin:2px 0 6px}
.founding p{width:500px;margin:0 auto 10px;color:var(--muted)}

/* video */
.video{height:130px;background:var(--red);display:flex;align-items:center;gap:22px;padding:0 40px}
.video-photo{width:210px;height:104px;background:linear-gradient(120deg,#c9a88a,#e6d4c0 50%,#8a6a50)}
.video-body{color:var(--white);flex:1}
.video-body h3{font-size:15px;font-weight:400;margin-bottom:4px}
.video-body p{margin-bottom:10px}

/* blog */
.blog{height:235px;padding-top:12px}
.blog .section-title{text-align:center;margin-bottom:10px}
.cards{display:flex;gap:16px}
.card{flex:1}
.card-photo{height:82px;position:relative}
.card:nth-child(1) .card-photo{background:linear-gradient(135deg,#9aa3a8,#5d6a70)}
.card:nth-child(2) .card-photo{background:linear-gradient(135deg,#f0b45a,#7fa84c)}
.card:nth-child(3) .card-photo{background:linear-gradient(135deg,#e8e2d8,#b9a48a)}
.card-caption{position:absolute;left:0;right:0;bottom:0;background:rgba(0,0,0,.45);color:var(--white);padding:3px 5px;font-size:6.5px}
.card-date{color:var(--red);font-weight:600;margin:5px 0 2px}
.card p{color:var(--muted);margin-bottom:8px}

/* about */
.about{height:190px;background:var(--light);display:flex;align-items:center;gap:24px;padding:0 40px}
.founder{width:150px;height:150px;position:relative;background:linear-gradient(160deg,#c9ccd1,#8e939b)}
.founder-caption{position:absolute;left:0;right:0;bottom:0;background:rgba(255,255,255,.85);text-align:center;padding:3px;font-weight:600;color:var(--navy)}
.about-body{flex:1}
.about-body h3{font-size:15px;font-weight:400;color:var(--blue);margin-bottom:4px}
.about-body p{color:var(--muted);margin-bottom:10px}

/* footer */
.site-footer{height:185px;background:var(--navy);color:var(--white);display:flex;gap:24px;padding:22px 40px 0}
.col{flex:1}
.col h4{font-size:8px;font-weight:600;margin-bottom:8px}
.col li{list-style:none;font-size:6.5px;margin-bottom:3px;color:#c8d4e6}
.col p{color:#c8d4e6;font-size:6.5px}
.socials{display:flex;gap:4px}
.socials span{width:14px;height:14px;border-radius:50%;display:block}
.subscribe{display:flex}
.subscribe span{flex:1;background:var(--white);color:#999;font-size:6.5px;padding:4px}
.subscribe b{background:var(--red);font-size:6.5px;padding:4px 10px;font-weight:600}
.copyright{height:20px;background:var(--blue-dark);color:#c8d4e6;font-size:6px;display:flex;align-items:center;justify-content:center}
</style>
</head>
<body>
<header class="site-header">
  <div class="brand"><span class="brand-mark"></span><span class="brand-name">Nutrient Guild of Meridia</span></div>
  <div class="header-tools">
    <span class="login">Login</span>
    <span class="search"><svg width="7" height="7" viewBox="0 0 10 10"><circle cx="4" cy="4" r="3" fill="none" stroke="#0355a3" stroke-width="1.4"/><line x1="6.2" y1="6.2" x2="9" y2="9" stroke="#0355a3" stroke-width="1.4"/></svg></span>
  </div>
</header>

<section class="hero" role="img" aria-label="Smiling woman surrounded by fresh vegetables and fruit">
  <h1 class="hero-title">" Tristique semper eltum tor lacus"</h1>
</section>

<nav class="main-nav">
  <a class="active">Home</a><a>About Us</a><a>Our Contacts</a><a>Membership Opportunities</a><a>Video Library</a>
</nav>

<section class="founding">
  <h2 class="section-title">Seeking Founding Members</h2>
  <div class="sub">Food for Micronutrient Thought</div>
  <p>We are searching for forward-minded members who want to help shape how our guild shares nutrition research with scientists, media, medical professionals and the public. Founding members set early priorities and receive first access to events, reports and our growing video library.</p>
  <span class="btn btn-blue">Join us Today</span>
</section>

<section class="video">
  <div class="video-photo" role="img" aria-label="Two women laughing together over a meal"></div>
  <div class="video-body">
    <h3>Video Library</h3>
    <p>Posted on September 3, 2014 by Admin. Our annual summit gathered researchers and practitioners to discuss new findings on vitamins, minerals and daily wellbeing. The full recording is now in the library.</p>
    <span class="btn btn-blue">Read More</span>
  </div>
</section>

<section class="blog wrap">
  <h2 class="section-title">Latest Blog</h2>
  <div class="cards">
    <article class="card">
      <div class="card-photo" role="img" aria-label="Person working at a laptop"><div class="card-caption">Lorem ipsum dolor sit amet, consectetur adipiscing elit sed do.</div></div>
      <div class="card-date">July 28, 2015</div>
      <p>Lorem ipsum dolor sit amet, consectetur adipiscing elit, sed do eiusmod tempor incididunt ut labore et dolore magna aliqua. Ut enim ad minim veniam, quis nostrud exercitation ullamco laboris.</p>
      <span class="btn btn-red">Read More</span>
    </article>
    <article class="card">
      <div class="card-photo" role="img" aria-label="Fresh citrus fruit and vegetables"><div class="card-caption">Lorem ipsum dolor sit amet, consectetur adipiscing elit sed do.</div></div>
      <div class="card-date">July 28, 2015</div>
      <p>Lorem ipsum dolor sit amet, consectetur adipiscing elit, sed do eiusmod tempor incididunt ut labore et dolore magna aliqua. Ut enim ad minim veniam, quis nostrud exercitation ullamco laboris.</p>
      <span class="btn btn-red">Read More</span>
    </article>
    <article class="card">
      <div class="card-photo" role="img" aria-label="Doctor talking with a patient"><div class="card-caption">Lorem ipsum dolor sit amet, consectetur adipiscing elit sed do.</div></div>
      <div class="card-date">July 28, 2015</div>
      <p>Lorem ipsum dolor sit amet, consectetur adipiscing elit, sed do eiusmod tempor incididunt ut labore et dolore magna aliqua. Ut enim ad minim veniam, quis nostrud exercitation ullamco laboris.</p>
      <span class="btn btn-red">Read More</span>
    </article>
  </div>
</section>

<section class="about">
  <div class="founder" role="img" aria-label="Portrait of the guild founder">
    <div class="founder-caption">Marcus T. Ellison, BSc, MPH<br>NGM Founder &amp; CEO</div>
  </div>
  <div class="about-body">
    <h3>About Us</h3>
    <p>Marcus T. Ellison founded the Nutrient Guild of Meridia to bring clear, evidence-based guidance on vitamins and minerals to everyone. The guild connects researchers, clinicians and educators, supports independent studies, and shares practical resources so that families can make confident choices about their daily nutrition and long-term health.</p>
    <span class="btn btn-blue">Read More</span>
  </div>
</section>

<footer class="site-footer">
  <div class="col">
    <h4>The gallery</h4>
    <ul><li>HOME</li><li>ABOUT US</li><li>CONTACT US</li><li>MEMBERSHIP OPPORTUNITIES</li><li>VIDEO LIBRARY</li></ul>
  </div>
  <div class="col">
    <h4>Articles</h4>
    <p>Lorem ipsum dolor sit amet, consectetur adipiscing elit. Sed posuere consectetur est at lobortis.</p>
  </div>
  <div class="col">
    <h4>Get in Touch!</h4>
    <div class="socials"><span style="background:#3b5998"></span><span style="background:#29a9e0"></span><span style="background:#d34836"></span><span style="background:#0e76a8"></span></div>
  </div>
  <div class="col">
    <h4>News Letter Subscribe</h4>
    <div class="subscribe"><span>Enter Address</span><b>Send</b></div>
  </div>
</footer>
<div class="copyright">Copyright © 2015 All Rights Reserved</div>
</body>
</html>
```